Book Cover Design Project

I would like a book cover designed for a book entitled: Bright Days Ahead: Finding the Right Cosmetic Dentist
The target audience is those patients interested in cosmetic dentistry. Generally those would be people over 45, with above average income, but the cover should have more universal appeal.
The book was written by
Raymond T. Oakes, DDS, FSFDP
Fellow in the Society of Family Dental Practice
(that's me)
The book will be distributed as an ebook for free to patients and potential patients interested in cosmetic dentistry.

```html
<!DOCTYPE html>
<html lang="en">
<head>
<meta charset="utf-8">
<title>Bright Days Ahead – Book Cover</title>
<link rel="stylesheet" href="https://fonts.googleapis.com/css2?family=Tinos:wght@400;700&display=swap">
<style>
  :root {
    --stage: #e9e6e1;
    --paper: #ffffff;
    --title-red: #e0241b;
    --title-shadow: #5a0d08;
    --band-red: #e3261c;
    --ink: #141414;
    --band-text: #ffffff;
    --skin-light: #f6dccb;
    --skin-mid: #eab79c;
    --hair: #d9b66e;
  }
  html, body {
    margin: 0;
    padding: 0;
    width: 1200px;
    height: 900px;
    overflow: hidden;
    background: var(--stage);
  }
  .canvas {
    position: relative;
    width: 1200px;
    height: 900px;
  }
  .book-cover {
    position: absolute;
    left: 282px;
    top: 40px;
    width: 636px;
    height: 820px;
    background: var(--paper);
    overflow: hidden;
    box-shadow: 0 6px 24px rgba(0,0,0,0.25);
    font-family: "Tinos", "Times New Roman", serif;
  }
  .cover-photo {
    position: absolute;
    left: 0;
    top: 0;
    width: 520px;
    height: 612px;
    background:
      radial-gradient(ellipse 60% 45% at 30% 20%, var(--hair) 0%, rgba(217,182,110,0) 70%),
      radial-gradient(ellipse 70% 70% at 35% 55%, var(--skin-mid) 0%, var(--skin-light) 45%, rgba(255,255,255,0) 80%);
  }
  .cover-title {
    position: absolute;
    left: 310px;
    top: 150px;
    margin: 0;
    font-weight: 700;
    font-size: 98px;
    line-height: 0.97;
    color: var(--title-red);
    text-shadow:
      -2px -2px 0 var(--paper), 2px -2px 0 var(--paper),
      -2px 2px 0 var(--paper), 2px 2px 0 var(--paper),
      5px 5px 4px var(--title-shadow);
  }
  .cover-title span { display: block; }
  .cover-subtitle {
    position: absolute;
    left: 348px;
    top: 468px;
    margin: 0;
    font-weight: 700;
    font-size: 26px;
    line-height: 1.2;
    color: var(--ink);
  }
  .author-band {
    position: absolute;
    left: 0;
    top: 612px;
    width: 100%;
    height: 126px;
    background: var(--band-red);
    box-sizing: border-box;
    padding: 22px 0 0 44px;
    color: var(--band-text);
  }
  .author-name {
    margin: 0;
    font-weight: 700;
    font-size: 31px;
    line-height: 1.2;
  }
  .author-credential {
    margin: 4px 0 0;
    font-weight: 700;
    font-size: 20px;
    line-height: 1.2;
  }
</style>
</head>
<body>
<main class="canvas">
  <article class="book-cover">
    <div class="cover-photo" role="img" aria-label="Close-up photograph of a smiling blonde woman looking upward"></div>
    <h1 class="cover-title"><span>Bright</span><span>Days</span><span>Ahead</span></h1>
    <p class="cover-subtitle">Finding the Right<br>Cosmetic Dentist</p>
    <footer class="author-band">
      <p class="author-name">Raymond T. Oakes, DDS, FSFDP</p>
      <p class="author-credential">Fellow in the Society of Family Dental Practice</p>
    </footer>
  </article>
</main>
</body>
</html>
```